Graphical Enhancement of Existing WordPress Website, 4 Landing Pages and 5 Social Sites

This project involves graphically enhancing already existing web pages. The website, landing pages and social pages were developed in the last couple of months using WordPress.
We have a newly developed website (20 - 30 pages), 4 landing pages and 5 social sites. The website has one design for the home page and one different design for most of the secondary pages with varying graphics. The 4 landing pages are identical except for one photo per page and two colors. The 5 social sites are not yet complete but will be soon.
The look and feel of all of these is OK but not great. We want the pages revised by a graphic designer/web designer so that they look very, very pleasing. We want to convey a feeling of business polish, smart, but not heavy corporate. The images for individual pages should reinforce the content of the page. The layout and function of the main website and landing pages would probably not change significantly but we are open to suggestion. Primarily we just want to go from OK looking to great looking. This might involve primarily improvements to the colors, fonts and/or images.
Lastly, some designers/developers prefer email and do not like talking much. We require the ability to talk frequenlty, probably on Skype.
Please submit one graphical enhancement of this page:
http://www.parcel-checkpoint.example/
and one graphical enhancement of this page:
http://www.brixolux.example/web/
Reason: I would like to see more designs.
I can absolutley guarantee payment and would be happy to escrow the funds if I see a design I like.
Reason: We found a design we liked and tried to communicate with the designer. The designer has been unresponsive for a week or two. We can't hire someone who does not respond.
We sell software to large companies (Meridian 400). Potential customers for our software are large enterprises with large CRM deployments in the US and Canada.
Business

```html
<!DOCTYPE html>
<html lang="en">
<head>
<meta charset="utf-8">
<title>Norvale Data – Enterprise Data Quality Made Easy</title>
<link href="https://fonts.googleapis.com/css2?family=Open+Sans:ital,wght@0,400;0,600;0,700;1,700&family=Oswald:wght@700&display=swap" rel="stylesheet">
<style>
:root{
  --navy:#142a6c;
  --link:#1d3a8f;
  --text:#333;
  --muted:#4a4a4a;
  --band:#dedede;
  --rule:#f2f2f2;
  --yellow:#f9b800;
  --orange:#f08c00;
  --white:#fff;
}
*{margin:0;padding:0;box-sizing:border-box}
html,body{width:784px;height:1200px;overflow:hidden;background:var(--white)}
body{position:relative;font-family:"Open Sans",Arial,sans-serif;color:var(--text)}
a{color:inherit;text-decoration:none}

.site-header{position:absolute;left:0;top:0;width:784px;height:116px}
.brand{position:absolute;left:42px;top:30px;display:flex;align-items:center;gap:8px}
.brand-dot{width:18px;height:18px;border-radius:50%;background:var(--yellow)}
.brand-name{font-size:28px;font-weight:700;color:var(--navy);letter-spacing:-.5px;line-height:1}
.brand-tag{position:absolute;left:125px;top:67px;font-size:10px;color:#222}
.contact{position:absolute;right:39px;top:25px;text-align:right}
.contact small{display:block;font-size:9px;color:#444}
.contact strong{display:block;font-size:15px;font-weight:600;color:#444;margin-top:-1px}
.main-nav{position:absolute;right:39px;top:68px;display:flex;gap:37px;font-size:12px;color:var(--link)}

.grey-band{position:absolute;left:0;top:333px;width:784px;height:399px;background:var(--band)}
.hero-photo{position:absolute;left:33px;top:116px;width:719px;height:298px;
  background:linear-gradient(100deg,#c8b08a 0%,#a88a66 30%,#6d6a68 55%,#b7b9c0 80%,#d9d6cf 100%)}
.promo-bar{position:absolute;left:33px;top:414px;width:719px;height:45px;background:var(--navy);
  display:flex;align-items:center;padding-left:14px;color:var(--white);font-size:14.5px;font-weight:700;font-style:italic}
.promo-bar span+span{margin-left:18px}
.trial-btn{position:absolute;right:12px;top:8px;width:195px;height:28px;background:var(--yellow);border-radius:3px;
  display:flex;align-items:center;justify-content:center;font-size:14px;font-weight:700;font-style:italic;color:var(--white);letter-spacing:.3px}

.features{position:absolute;left:0;top:476px;width:784px}
.feature-row{position:relative;height:80px;border-bottom:1px solid var(--rule)}
.feature-row+.feature-row{height:88px}
.feature{position:absolute;top:16px}
.feature svg{position:absolute;left:0;top:0;width:32px;height:34px}
.feature h3{margin-left:39px;font-size:11.2px;font-weight:700;color:var(--link);line-height:1.05;letter-spacing:-.1px}
.feature p{margin-left:39px;font-size:8.4px;color:var(--muted);line-height:1.12;margin-top:2px}
.feature p em{font-style:normal;color:var(--orange)}
.c1{left:8px;width:258px}.c2{left:271px;width:256px}.c3{left:528px;width:256px}

.about{position:absolute;left:23px;top:783px;width:388px}
.about h1{font-family:"Oswald",Arial,sans-serif;font-size:32px;font-weight:700;color:var(--navy);letter-spacing:-.5px;line-height:1}
.about .lead{margin-top:14px;font-size:11.4px;line-height:1.16;padding-right:30px}
.about h2{margin-top:13px;font-size:14.5px;font-weight:600;color:#333;line-height:1.1}
.about p{font-size:11.4px;line-height:1.16}

.blog{position:absolute;left:443px;top:786px;width:320px}
.blog h2{font-size:14.5px;font-weight:700;color:var(--navy);line-height:1.2}
.post{margin-top:14px}
.blog h2+.post{margin-top:17px}
.post h3{font-size:11.2px;font-weight:600;color:#333;line-height:1.1}
.post p{font-size:8.9px;line-height:1.3;color:var(--muted)}

.site-footer{position:absolute;left:0;top:1117px;width:784px;height:51px;background:var(--navy);color:var(--white);
  display:flex;align-items:center;justify-content:space-between;padding:0 26px 0 19px;font-size:15.5px}
.legal{position:absolute;left:22px;top:1178px;width:733px;display:flex;justify-content:space-between;font-size:9.5px;color:var(--link)}
.legal span.sep{margin:0 5px;color:#666}
</style>
</head>
<body>

<header class="site-header">
  <a class="brand" href="#"><span class="brand-dot"></span><span class="brand-name">Norvale Data</span></a>
  <div class="brand-tag">Enterprise Data Quality Made Easy</div>
  <div class="contact"><small>For questions and inquiries</small><strong>Call (555) 014-2237</strong></div>
  <nav class="main-nav"><a href="#">Connectors</a><a href="#">Data Cleansing</a><a href="#">Special Offers</a><a href="#">Services</a></nav>
</header>

<div class="grey-band"></div>
<div class="hero-photo" role="img" aria-label="Photo of two young professionals sitting by a waterfront, one working on a laptop"></div>

<div class="promo-bar">
  <span>Correct and Verify 20,000 Addresses for Free!</span>
  <span>It’s Easy with VQ*Core</span>
  <a class="trial-btn" href="#">START YOUR FREE TRIAL</a>
</div>

<section class="features">
  <div class="feature-row">
    <div class="feature c1">
      <svg viewBox="0 0 32 34" fill="none" stroke="#142a6c" stroke-width="2"><circle cx="16" cy="17" r="14"/><ellipse cx="16" cy="17" rx="6" ry="14"/><path d="M2 17h28M5 9h22M5 25h22M16 3v28"/></svg>
      <h3>US and International Addresses</h3>
      <p>VQ*Core provides a single solution for all of<br>your address validation needs.</p>
    </div>
    <div class="feature c2">
      <svg viewBox="0 0 32 34"><rect x="1" y="6" width="30" height="22" fill="#142a6c"/><path d="M2 7l14 12L30 7M2 27l10-10M30 27L20 17" stroke="#fff" stroke-width="2" fill="none"/></svg>
      <h3>Unit Point Check and<br>Address Move Update (AMU)</h3>
      <p>Reduce postal costs and make sure your mail<br>reaches its intended target.</p>
    </div>
    <div class="feature c3">
      <svg viewBox="0 0 32 34" fill="none" stroke="#142a6c" stroke-width="2"><rect x="3" y="3" width="20" height="28"/><path d="M7 10h12M7 15h12M7 20h12M7 25h8"/><path d="M28 6v24" stroke-width="3"/></svg>
      <h3>Geocoding and More</h3>
      <p>VQ*Core fills in the blanks with Name, Address,<br>Phone, Email, Geographic Coordinates ...</p>
    </div>
  </div>
  <div class="feature-row">
    <div class="feature c1">
      <svg viewBox="0 0 32 34"><rect x="4" y="4" width="26" height="22" fill="#142a6c"/><rect x="7" y="9" width="20" height="14" fill="#fff"/><rect x="1" y="12" width="14" height="20" fill="#142a6c"/><rect x="3" y="16" width="10" height="13" fill="#fff"/></svg>
      <h3 style="white-space:nowrap">Address Validation in Your Application</h3>
      <p>VQ*Core has application aware connectors for<br><em>Corvian Business Suite</em>, <em>Cloudledger.example</em> and<br><em>Tessaro</em>.</p>
    </div>
    <div class="feature c2">
      <svg viewBox="0 0 32 34" fill="#142a6c"><rect x="2" y="2" width="20" height="8"/><rect x="2" y="12" width="20" height="8"/><rect x="2" y="22" width="20" height="8"/><rect x="16" y="16" width="15" height="16" stroke="#fff" stroke-width="1.5"/></svg>
      <h3 style="white-space:nowrap">Address Validation in Your Database</h3>
      <p>VQ*Core has database aware connectors for<br>Quarry DB, Halden SQL Server and Corvian.</p>
    </div>
    <div class="feature c3">
      <svg viewBox="0 0 32 34"><rect x="1" y="2" width="30" height="22" fill="#142a6c"/><rect x="5" y="6" width="22" height="14" fill="#fff"/><path d="M9 9h14M9 13h14M9 17h10" stroke="#142a6c" stroke-width="1.5"/><rect x="13" y="24" width="6" height="5" fill="#142a6c"/><rect x="8" y="29" width="16" height="3" fill="#142a6c"/></svg>
      <h3 style="white-space:nowrap">Address Validation on Your Website</h3>
      <p>Embed address verification on your websites<br>with VQ*Core Web Service APIs.</p>
    </div>
  </div>
  <div class="feature-row" style="border-bottom:0">
    <div class="feature c1">
      <svg viewBox="0 0 32 34" fill="none" stroke="#142a6c" stroke-width="3"><circle cx="12" cy="13" r="8"/><circle cx="25" cy="26" r="5" stroke-width="2.5"/><circle cx="12" cy="13" r="2.5" fill="#142a6c" stroke="none"/></svg>
      <h3>Real Time Address Verification</h3>
      <p>VQ*Core automatically fills in address data as<br>you type and prevents the entry of bad data.</p>
    </div>
    <div class="feature c2">
      <svg viewBox="0 0 32 34"><rect x="1" y="6" width="30" height="22" fill="#142a6c"/><path d="M2 7l14 12L30 7M2 27l10-10M30 27L20 17" stroke="#fff" stroke-width="2" fill="none"/></svg>
      <h3>Batch Address Verification</h3>
      <p>VQ*Core is enterprise scale and will validate<br>high volumes of addresses in batch mode.</p>
    </div>
    <div class="feature c3">
      <svg viewBox="0 0 32 34" fill="#142a6c"><circle cx="16" cy="11" r="8"/><path d="M3 34c0-9 6-13 13-13s13 4 13 13z"/><path d="M7 11a9 9 0 0 1 18 0" stroke="#142a6c" stroke-width="2" fill="none"/></svg>
      <h3>Professional Services</h3>
      <p>Norvale Data consultants are Customer Data<br>experts. We provide cost effective services to<br>solve your biggest data challenges.</p>
    </div>
  </div>
</section>

<section class="about">
  <h1>WHAT IS VQ*CORE</h1>
  <p class="lead">VQ*Core is a data quality software solution that was designed to meet the needs of large enterprises.</p>
  <h2>US Address Verification</h2>
  <p>The VQ*Core address verification engine is PAVE Certified by the NPS. VQ*Core address processing uses the latest NPS data file to validate addresses to the street number range and apply the Postcode+4 code. VQ*Core also provides Unit Point Check (UPC) which can validate the existence of an address to the street number and secondary unit number based on the latest NPS data file. Additional data may be appended during address processing, such as suite, carrier route code, delivery point barcode, county name, latitude and longitude coordinates, time zone and US census data.</p>
  <h2>International Address Verification</h2>
  <p>VQ*Core corrects, verifies and standardizes address data for over 200 countries using rules that comply with local postal standards and address data files provided by the postal authorities from each country.</p>
</section>

<aside class="blog">
  <h2>Norvale Data Blog – Data quality, enterprise project management and other items of interest</h2>
  <article class="post"><h3>Welcome to the Norvale Data Blog</h3><p>VQ*Core data quality software provides a single solution for all of your address validation needs. The post Welcome to the Norvale Data Blog appeared first on Data Quality Software, Norvale Data.</p></article>
  <article class="post"><h3>Welcome to the Norvale Data Blog</h3><p>VQ*Core data quality software provides a single solution for all of your address validation needs. The post Welcome to the Norvale Data Blog appeared first on Data Quality Software, Norvale Data.</p></article>
  <article class="post"><h3>Welcome to the Norvale Data Blog</h3><p>VQ*Core data quality software provides a single solution for all of your address validation needs. The post Welcome to the Norvale Data Blog appeared first on Data Quality Software, Norvale Data.</p></article>
  <article class="post"><h3>Welcome to the Norvale Data Blog</h3><p>VQ*Core data quality software provides a single solution for all of your address validation needs. The post Welcome to the Norvale Data Blog appeared first on Data Quality Software, Norvale Data.</p></article>
</aside>

<footer class="site-footer">
  <span>Correct and Verify 20,000 Addresses for Free!</span>
  <span>Enterprise Data Quality Made Easy</span>
</footer>
<div class="legal">
  <div><a href="#">Norvale Data</a><span class="sep">|</span><a href="#">Email Us</a></div>
  <div>All content copyright © 2013</div>
</div>

</body>
</html>
```